Business Card Design

We are a commercial real estate brokerage in San Francisco, leasing office buildings downtown.
I would like a clean, elegant look. Simple but powerful .

Industry/Entity Type

Business

Contact Information for Business Card

Derek Hollings
lic# 02875140
415.287.6041
derek@vexa-commercial.com
vexa-commercial.com

```html
<!DOCTYPE html>
<html lang="en">
<head>
<meta charset="utf-8">
<title>Vexa Commercial — Business Card</title>
<link rel="stylesheet" href="https://fonts.googleapis.com/css2?family=Montserrat:wght@400;500;600;700&display=swap">
<style>
  :root {
    --backdrop: #e6e7ea;
    --card: #ffffff;
    --brand-blue: #5f7399;
    --ink: #2e2f33;
    --ink-soft: #4a4b50;
    --skyline-light: #f3f3f4;
    --skyline-mid: #e9e9eb;
  }
  * { box-sizing: border-box; margin: 0; padding: 0; }
  html, body {
    width: 1200px; height: 720px; overflow: hidden;
    background: var(--backdrop);
    font-family: "Montserrat", Arial, sans-serif;
  }
  .canvas {
    position: relative; width: 1200px; height: 720px;
    display: flex; align-items: center; justify-content: center;
  }
  .business-card {
    position: relative; width: 1000px; height: 572px;
    background: var(--card);
    box-shadow: 0 6px 24px rgba(0,0,0,0.12);
    overflow: hidden;
  }
  .skyline-art {
    position: absolute; right: 0; bottom: 0;
    width: 520px; height: 470px;
    background: linear-gradient(180deg, var(--skyline-light) 0%, var(--skyline-mid) 100%);
    clip-path: polygon(0 38%, 14% 38%, 14% 20%, 34% 20%, 34% 8%, 52% 8%, 52% 28%, 66% 28%, 66% 0, 84% 0, 84% 16%, 100% 16%, 100% 100%, 0 100%);
  }
  .brand {
    position: absolute; left: 78px; top: 92px;
    display: flex; align-items: center; gap: 22px;
  }
  .brand-square {
    width: 56px; height: 56px; background: var(--brand-blue);
  }
  .brand-name {
    font-size: 52px; font-weight: 700; color: var(--brand-blue);
    letter-spacing: 1px; line-height: 1;
  }
  .contact {
    position: absolute; left: 78px; top: 292px;
    color: var(--ink);
  }
  .contact-name {
    font-size: 34px; font-weight: 700; color: var(--brand-blue);
    margin-bottom: 26px;
  }
  .contact-line {
    display: flex; align-items: center; gap: 14px;
    font-size: 24px; font-weight: 500; color: var(--ink-soft);
    margin-bottom: 12px; line-height: 1.2;
  }
  .contact-line.license { margin-left: 0; }
  .contact-line .icon { width: 24px; height: 24px; flex: none; }
  .contact-line.with-icon { margin-left: 0; }
  .web-domain { color: var(--brand-blue); font-weight: 700; }
</style>
</head>
<body>
<main class="canvas">
  <article class="business-card">
    <div class="skyline-art" role="img" aria-label="Faint downtown skyline illustration"></div>

    <header class="brand">
      <span class="brand-square"></span>
      <span class="brand-name">Vexa Commercial</span>
    </header>

    <section class="contact">
      <h1 class="contact-name">Derek Hollings</h1>
      <p class="contact-line license">Lic # 02875140</p>
      <p class="contact-line with-icon">
        <svg class="icon" viewBox="0 0 24 24" aria-hidden="true"><path fill="#5f7399" d="M6.6 10.8a15.1 15.1 0 0 0 6.6 6.6l2.2-2.2a1 1 0 0 1 1-.25 11.4 11.4 0 0 0 3.6.57 1 1 0 0 1 1 1V20a1 1 0 0 1-1 1A17 17 0 0 1 3 4a1 1 0 0 1 1-1h3.5a1 1 0 0 1 1 1c0 1.25.2 2.45.57 3.57a1 1 0 0 1-.25 1z"/></svg>
        415.287.6041
      </p>
      <p class="contact-line with-icon">
        <svg class="icon" viewBox="0 0 24 24" aria-hidden="true"><rect x="2" y="5" width="20" height="14" rx="1.5" fill="#5f7399"/><path d="M3 6.5l9 6.5 9-6.5" fill="none" stroke="#fff" stroke-width="1.6"/></svg>
        derek@vexa-commercial.com
      </p>
      <p class="contact-line with-icon">
        <svg class="icon" viewBox="0 0 24 24" aria-hidden="true"><circle cx="12" cy="12" r="10" fill="#5f7399"/><path d="M2 12h20M12 2c3 3 3 17 0 20M12 2c-3 3-3 17 0 20" fill="none" stroke="#fff" stroke-width="1.4"/></svg>
        <span>www.<span class="web-domain">vexa-commercial</span>.com</span>
      </p>
    </section>
  </article>
</main>
</body>
</html>
```